Refresh of Business Card Design

Want to refresh the business card design with the new logo while adhering to style guide as attached. Would like to match feel of website www.brimwickdrives.com

```html
<!DOCTYPE html>
<html lang="en">
<head>
<meta charset="utf-8">
<title>Brimwick Drives – Stationery Set</title>
<link href="https://fonts.googleapis.com/css2?family=PT+Sans:wght@400;700&display=swap" rel="stylesheet">
<style>
  :root {
    --sheet-bg: #6a9468;
    --paper: #ffffff;
    --brand-red: #e0242c;
    --brand-red-dark: #b81a20;
    --ink: #333333;
    --ink-soft: #555555;
    --black: #0d0d0d;
    --label: #ffffff;
  }
  * { box-sizing: border-box; margin: 0; padding: 0; }
  html, body { width: 1200px; height: 1200px; overflow: hidden; }
  body {
    background: var(--sheet-bg);
    font-family: "PT Sans", Arial, sans-serif;
    position: relative;
    color: var(--ink);
  }
  .piece { position: absolute; background: var(--paper); overflow: hidden; }
  .piece-label {
    position: absolute;
    color: var(--label);
    font-size: 15px;
    line-height: 1;
  }
  .red-band {
    position: absolute;
    left: 0; right: 0;
    background: linear-gradient(180deg, var(--brand-red) 0%, var(--brand-red) 70%, var(--brand-red-dark) 100%);
    box-shadow: 0 2px 4px rgba(0,0,0,0.25);
  }
  .wordmark {
    position: absolute;
    display: flex;
    align-items: center;
    gap: 8px;
    font-weight: 700;
    text-transform: uppercase;
    white-space: nowrap;
    letter-spacing: 0.5px;
  }
  .wordmark .dot {
    border-radius: 50%;
    background: var(--black);
    flex: none;
  }
  .wordmark.on-red { color: #ffffff; }
  .wordmark.on-white { color: var(--black); }

  .contact-list { position: absolute; list-style: none; color: var(--ink); }
  .contact-list li { display: flex; align-items: flex-start; gap: 6px; }
  .contact-list svg { flex: none; fill: var(--brand-red); }

  /* Logo panel */
  .logo-panel { left: 0; top: 0; width: 331px; height: 215px; }

  /* Letterhead */
  .letterhead { left: 606px; top: 94px; width: 544px; height: 706px; }
  .letterhead .red-band { top: 46px; height: 36px; }
  .letterhead .contact-list { left: 20px; top: 594px; font-size: 10.5px; }
  .letterhead .contact-list li { margin-bottom: 5px; line-height: 12px; }
  .letterhead .contact-list svg { width: 11px; height: 11px; margin-top: 1px; }

  /* Business card front */
  .card-front { left: 85px; top: 338px; width: 284px; height: 163px; }
  .card-front .red-band { top: 32px; height: 33px; }
  .holder { position: absolute; left: 10px; top: 36px; color: #ffffff; line-height: 1.15; }
  .holder .holder-name { font-size: 8px; font-weight: 700; text-transform: uppercase; }
  .holder .holder-role { font-size: 7px; }
  .card-front .contact-list { left: 10px; top: 88px; font-size: 7px; }
  .card-front .contact-list li { gap: 4px; line-height: 9px; margin-bottom: 2px; }
  .card-front .contact-list svg { width: 7px; height: 7px; margin-top: 1px; }

  /* Business card back */
  .card-back { left: 232px; top: 560px; width: 285px; height: 162px; }
  .card-back .red-band {
    top: 113px; height: 25px;
    display: flex; align-items: center; justify-content: center;
    color: #ffffff; font-size: 9px; font-weight: 700; letter-spacing: 3px;
  }

  /* Envelope front */
  .envelope-front { left: 51px; top: 874px; width: 527px; height: 227px; }
  .envelope-front .red-band { top: 40px; height: 33px; }
  .envelope-front .contact-list { left: 14px; top: 189px; font-size: 8px; }
  .envelope-front .contact-list li { line-height: 10px; gap: 4px; }
  .envelope-front .contact-list svg { width: 8px; height: 8px; margin-top: 1px; }

  /* Envelope back */
  .envelope-back { left: 624px; top: 874px; width: 526px; height: 227px; }
  .envelope-back svg { position: absolute; left: 0; top: 0; }
  .seal-dot { fill: #b81a20; stroke: #3a3a3a; stroke-width: 2; }
</style>
</head>
<body>

  <!-- Logo panel -->
  <section class="piece logo-panel">
    <div class="wordmark on-white" style="left:40px; top:92px; font-size:25px;">
      <span class="dot" style="width:26px; height:26px;"></span>Brimwick Drives
    </div>
  </section>

  <!-- Letterhead -->
  <span class="piece-label" style="left:606px; top:66px;">Letterhead_1</span>
  <section class="piece letterhead">
    <div class="red-band"></div>
    <div class="wordmark on-red" style="left:22px; top:52px; font-size:17px;">
      <span class="dot" style="width:22px; height:22px;"></span>Brimwick Drives
    </div>
    <ul class="contact-list">
      <li><svg viewBox="0 0 16 16"><path d="M3 1l3 3-2 2c1 2 3 4 5 5l2-2 3 3-2 3C7 15 1 9 0 3z"/></svg>555.210.4400</li>
      <li><svg viewBox="0 0 16 16"><path d="M4 1h8v4H4zM1 6h14v7h-3v2H4v-2H1zM5 10v4h6v-4z"/></svg>555.210.4417</li>
      <li><svg viewBox="0 0 16 16"><path d="M0 3h16v10H0zM1 4l7 5 7-5v-0z" /></svg>sales@brimwickdrives.com</li>
      <li><svg viewBox="0 0 16 16"><circle cx="8" cy="8" r="7"/></svg>www.brimwickdrives.com</li>
      <li><svg viewBox="0 0 16 16"><path d="M8 0a5 5 0 0 1 5 5c0 4-5 11-5 11S3 9 3 5a5 5 0 0 1 5-5z"/></svg><span>1840 N. Ridge Rd. 442 Carrow TX 79012<br>PO Box 52210 Carrow Texas 79015</span></li>
    </ul>
  </section>

  <!-- Business card front -->
  <span class="piece-label" style="left:85px; top:313px;">Business Card Front_1</span>
  <section class="piece card-front">
    <div class="red-band"></div>
    <div class="holder">
      <div class="holder-name">Dana Holloway</div>
      <div class="holder-role">CEO / Founder</div>
    </div>
    <div class="wordmark on-red" style="left:142px; top:40px; font-size:11px; gap:5px;">
      <span class="dot" style="width:15px; height:15px;"></span>Brimwick Drives
    </div>
    <ul class="contact-list">
      <li><svg viewBox="0 0 16 16"><path d="M3 1l3 3-2 2c1 2 3 4 5 5l2-2 3 3-2 3C7 15 1 9 0 3z"/></svg>555.210.4400</li>
      <li><svg viewBox="0 0 16 16"><path d="M4 1h8v4H4zM1 6h14v7h-3v2H4v-2H1zM5 10v4h6v-4z"/></svg>555.210.4417</li>
      <li><svg viewBox="0 0 16 16"><path d="M0 3h16v10H0z"/></svg>sales@brimwickdrives.com</li>
      <li><svg viewBox="0 0 16 16"><circle cx="8" cy="8" r="7"/></svg>www.brimwickdrives.com</li>
      <li><svg viewBox="0 0 16 16"><path d="M8 0a5 5 0 0 1 5 5c0 4-5 11-5 11S3 9 3 5a5 5 0 0 1 5-5z"/></svg><span>1840 N. Ridge Rd. 442 Carrow TX 79012<br>PO Box 52210 Carrow Texas 79015</span></li>
    </ul>
  </section>

  <!-- Business card back -->
  <span class="piece-label" style="left:232px; top:536px;">Business Card Back_1</span>
  <section class="piece card-back">
    <div class="wordmark on-white" style="left:78px; top:64px; font-size:13px; gap:6px;">
      <span class="dot" style="width:16px; height:16px;"></span>Brimwick Drives
    </div>
    <div class="red-band">www.brimwickdrives.com</div>
  </section>

  <!-- Envelope front -->
  <span class="piece-label" style="left:51px; top:849px;">Envelope Front_1</span>
  <section class="piece envelope-front">
    <div class="red-band"></div>
    <div class="wordmark on-red" style="left:16px; top:47px; font-size:15px;">
      <span class="dot" style="width:19px; height:19px;"></span>Brimwick Drives
    </div>
    <ul class="contact-list">
      <li><svg viewBox="0 0 16 16"><path d="M8 0a5 5 0 0 1 5 5c0 4-5 11-5 11S3 9 3 5a5 5 0 0 1 5-5z"/></svg><span>1840 N. Ridge Rd. 442 Carrow TX 79012<br>PO Box 52210 Carrow Texas 79015</span></li>
    </ul>
  </section>

  <!-- Envelope back -->
  <span class="piece-label" style="left:624px; top:849px;">Envelope Back_1</span>
  <section class="piece envelope-back">
    <svg width="526" height="227" viewBox="0 0 526 227" aria-hidden="true">
      <path d="M0 0H526L512 30Q505 42 478 45L300 82Q263 92 226 82L48 45Q21 42 14 30Z" fill="#0d0d0d"/>
      <circle class="seal-dot" cx="263" cy="64" r="16"/>
    </svg>
  </section>

</body>
</html>
```